Design mobile friendly review and ranking site

We're working on a corporate website for reviewing and ranking fellow employees. We need the website to look both fun and professional and it needs to be responsive - to it works on mobile and desktop.

Looking for css and HTML for 3 key pages as well as a header and footer for the site. Also would need any supporting graphics as part of the design.

Target Market(s)

Professionals in their 20s, 30s, and 40s.

Industry/Entity Type

Internet

Coding

Coded - Design and coding required

Number of Pages Required

3 page

Font styles to use
Sans Serif

Requirements
Must have
• 3 key pages we need (note included screenshots for each - these are just super rough cuts so you see examples of the content.)
• a) main-intro: A compelling into page with a login/registration form. Should be sleek/modern/enticing. Also we would show the ranking for the top 3 people to tease people re: content.
• b) main-page: Has two sections: One at the top where you would rate someone and one at the bottom where it shows a ranking of people.
• c) profile page: This is where you view a specific person. You see the person's picture, some info about the person, you see their overall rating, you can rate them, and you also see their historical ratings.
Nice to have
• Note we need css and HTML for this. It should feel as sleek and modern. Note also must be responsive design so it works well in mobile and desktop.

```html
<!DOCTYPE html>
<html lang="en">
<head>
<meta charset="utf-8">
<title>Peer Standing</title>
<link href="https://fonts.googleapis.com/css2?family=Lato:wght@300;400;700&display=swap" rel="stylesheet">
<style>
  :root {
    --orange: #f7a233;
    --orange-deep: #f08a12;
    --orange-text: #f39316;
    --navy: #16263a;
    --navy-mid: #243a55;
    --footer: #1f2a35;
    --ink: #333b44;
    --grey: #5a6068;
    --row-a: #efefef;
    --row-b: #f7f7f7;
    --white: #ffffff;
  }
  * { box-sizing: border-box; margin: 0; padding: 0; }
  html, body { width: 767px; height: 1200px; overflow: hidden; }
  body { font-family: "Lato", Arial, sans-serif; color: var(--ink); background: var(--white); position: relative; }

  /* Hero */
  .hero { position: absolute; left: 0; top: 0; width: 767px; height: 371px; overflow: hidden; }
  .hero-photo { position: absolute; inset: 0;
    background: radial-gradient(ellipse at 70% 60%, #3b4f6a 0%, var(--navy-mid) 35%, var(--navy) 80%); }
  .hero-photo::after { content: ""; position: absolute; left: 470px; top: 150px; width: 140px; height: 120px;
    border-radius: 50%; background: radial-gradient(ellipse, rgba(214,160,130,.55), rgba(214,160,130,0) 70%); }
  .brand { position: absolute; left: 57px; top: 20px; font-size: 14px; font-weight: 700; color: var(--orange); letter-spacing: .5px; }
  .nav-link { position: absolute; left: 528px; top: 24px; font-size: 9px; color: var(--white); letter-spacing: .3px; }
  .nav-link::after { content: ""; position: absolute; left: 16px; top: 16px; width: 43px; height: 2px; background: var(--orange); }
  .nav-btn { position: absolute; left: 633px; top: 18px; width: 80px; height: 22px; background: var(--orange);
    border-radius: 2px; color: var(--white); font-size: 8.5px; font-weight: 700; text-align: center; line-height: 22px; }
  .hero-title { position: absolute; left: 0; width: 767px; top: 120px; text-align: center; color: var(--white);
    font-size: 14.5px; letter-spacing: 1.3px; line-height: 17px; font-weight: 400; }
  .tabs { position: absolute; top: 243px; left: 0; width: 767px; height: 20px; }
  .tab { position: absolute; font-size: 9px; font-weight: 700; color: var(--white); }
  .tab-register { left: 331px; }
  .tab-login { left: 410px; }
  .tab::after { content: ""; position: absolute; left: -2px; right: -2px; top: 15px; height: 2px; background: var(--white); }
  .tab-register::after { background: var(--orange); }
  .form { position: absolute; left: 193px; top: 270px; width: 383px; height: 45px; background: rgba(255,255,255,.96); border-radius: 2px; }
  .form::before { content: ""; position: absolute; left: 153px; top: -5px; border: 5px solid transparent; border-top: 0; border-bottom-color: rgba(255,255,255,.96); }
  .form-input { position: absolute; left: 24px; top: 17px; font-size: 9px; color: #6a6f75; }
  .form-btn { position: absolute; left: 286px; top: 10px; width: 86px; height: 25px; background: var(--orange);
    border-radius: 2px; color: var(--white); font-size: 9px; line-height: 25px; padding-left: 13px; }
  .form-btn svg { position: absolute; right: 12px; top: 9px; }

  /* Welcome */
  .welcome-title { position: absolute; top: 411px; left: 0; width: 767px; text-align: center; color: var(--orange-text); font-size: 18px; font-weight: 400; }
  .welcome-rule { position: absolute; top: 440px; left: 361px; width: 46px; height: 2px; background: var(--orange); }
  .welcome-text { position: absolute; top: 453px; left: 106px; width: 556px; text-align: center; font-size: 7.6px; line-height: 11.8px; color: var(--grey); }

  /* Filter bar */
  .filter { position: absolute; top: 534px; left: 0; width: 767px; height: 39px; background: var(--orange); }
  .filter-select { position: absolute; left: 321px; top: 7px; width: 86px; height: 25px; background: var(--orange-deep);
    border-radius: 2px; color: var(--white); font-size: 8.5px; line-height: 25px; padding-left: 12px; }
  .filter-select svg { position: absolute; right: 10px; top: 10px; }
  .filter-label { position: absolute; left: 415px; top: 13px; color: var(--white); font-size: 8.5px; font-weight: 700; }

  /* Ranking rows */
  .rank-row { position: absolute; left: 0; width: 767px; height: 129px; }
  .row-1 { top: 573px; background: var(--row-a); }
  .row-2 { top: 702px; background: var(--row-b); }
  .row-3 { top: 830px; background: var(--row-a); }
  .avatar { position: absolute; left: 206px; top: 26px; width: 79px; height: 79px; border-radius: 50%;
    background: linear-gradient(160deg, #d9c1b0, #a88a77 60%, #6d5b52); }
  .rank-badge { position: absolute; right: 380px; top: 54px; font-size: 7.5px; color: var(--orange-text); }
  .person-name { position: absolute; right: 379px; top: 64px; font-size: 16px; font-weight: 400; color: #3a3f45; white-space: nowrap; letter-spacing: .2px; }
  .divider { position: absolute; left: 397px; top: 37px; width: 1px; height: 58px; background: #dcdcdc; }
  .stats { position: absolute; right: 274px; top: 36px; text-align: right; font-size: 7.8px; line-height: 13.6px; color: var(--ink); font-weight: 400; }
  .stats b { font-weight: 700; }
  .ratings { position: absolute; left: 514px; top: 49.6px; font-size: 7.8px; line-height: 13.6px; }
  .view-link { display: block; color: var(--orange-text); font-weight: 700; }
  .stars { display: block; height: 13.6px; padding-top: 3px; }

  /* Call to action */
  .cta-title { position: absolute; top: 991px; left: 0; width: 767px; text-align: center; font-size: 17px; font-weight: 400; color: var(--orange-text); }
  .cta-text { position: absolute; top: 1017px; left: 0; width: 767px; text-align: center; font-size: 11px; color: #444; }
  .cta-text b { font-weight: 700; }
  .cta-rule { position: absolute; top: 1037px; height: 2px; }
  .cta-rule.login { left: 323px; width: 32px; background: var(--orange); }
  .cta-rule.register { left: 368px; width: 43px; background: #9a9a9a; }

  /* Footer */
  .footer { position: absolute; top: 1066px; left: 0; width: 767px; height: 134px; background: var(--footer); text-align: center; color: var(--white); }
  .footer-brand { position: absolute; top: 27px; left: 0; width: 767px; font-size: 14px; font-weight: 700; color: var(--orange); letter-spacing: .5px; }
  .footer-nav { position: absolute; top: 58px; left: 0; width: 767px; font-size: 6.6px; letter-spacing: .4px; }
  .footer-nav span { margin: 0 5px; }
  .social { position: absolute; top: 81px; left: 0; width: 767px; line-height: 6px; }
  .social i { display: inline-block; width: 5px; height: 5px; border-radius: 50%; background: var(--white); margin: 0 5px; }
  .copyright { position: absolute; top: 101px; left: 0; width: 767px; font-size: 6.6px; font-weight: 700; }
</style>
</head>
<body>
<svg width="0" height="0" style="position:absolute">
  <defs>
    <symbol id="star" viewBox="0 0 10 10"><path d="M5 .4l1.4 3 3.2.3-2.4 2.1.7 3.2L5 7.3 2.1 9l.7-3.2L.4 3.7l3.2-.3z" fill="#f7a233"/></symbol>
  </defs>
</svg>

<header class="hero">
  <div class="hero-photo" role="img" aria-label="Businessman in a dark suit drawing a row of five yellow rating stars"></div>
  <div class="brand">PEER STANDING</div>
  <div class="nav-link">GET REGISTERED</div>
  <div class="nav-btn">LOGIN</div>
  <h1 class="hero-title">To see how people are ranked in your company<br>login or register</h1>
  <div class="tabs">
    <span class="tab tab-register">REGISTER</span>
    <span class="tab tab-login">LOGIN</span>
  </div>
  <div class="form">
    <span class="form-input">Your Work Email</span>
    <span class="form-btn">REGISTER
      <svg width="5" height="8" viewBox="0 0 5 8"><path d="M1 1l3 3-3 3" stroke="#fff" stroke-width="1" fill="none"/></svg>
    </span>
  </div>
</header>

<section>
  <h2 class="welcome-title">WELCOME</h2>
  <div class="welcome-rule"></div>
  <p class="welcome-text">Lorem ipsum dolor sit amet, consectetuer adipiscing elit, sed diam nonummy nibh euismod tincidunt ut laoreet dolore magna aliquam erat volutpat. Ut wisi enim ad minim veniam, quis nostrud exerci tation ullamcorper suscipit lobortis nisl ut aliquip ex ea commodo consequat. Duis autem vel eum iriure dolor in hendrerit in vulputate velit esse molestie consequat, vel illum dolore eu feugiat nulla facilisis at vero eros et accumsan et iusto odio dignissim qui blandit praesent luptatum zzril delenit augue duis dolore te feugait nulla facilisi.</p>
</section>

<div class="filter">
  <span class="filter-select">BEST
    <svg width="8" height="5" viewBox="0 0 8 5"><path d="M1 1l3 3 3-3" stroke="#fff" stroke-width="1" fill="none"/></svg>
  </span>
  <span class="filter-label">PEOPLE</span>
</div>

<article class="rank-row row-1">
  <div class="avatar" role="img" aria-label="Portrait photo of the ranked employee"></div>
  <span class="rank-badge">#1 Best</span>
  <span class="person-name">Sam Keller</span>
  <div class="divider"></div>
  <div class="stats">Points: <b>15</b><br>Number of reviews: <b>1</b><br>Smarts<br>Easy to work with<br>Hard worker</div>
  <div class="ratings">
    <span class="view-link">View Details</span>
    <span class="stars"><svg width="52" height="7"><use href="#star" width="7" height="7"/><use href="#star" x="11" width="7" height="7"/><use href="#star" x="22" width="7" height="7"/><use href="#star" x="33" width="7" height="7"/><use href="#star" x="44" width="7" height="7"/></svg></span>
    <span class="stars"><svg width="52" height="7"><use href="#star" width="7" height="7"/><use href="#star" x="11" width="7" height="7"/><use href="#star" x="22" width="7" height="7"/><use href="#star" x="33" width="7" height="7"/><use href="#star" x="44" width="7" height="7"/></svg></span>
    <span class="stars"><svg width="52" height="7"><use href="#star" width="7" height="7"/><use href="#star" x="11" width="7" height="7"/><use href="#star" x="22" width="7" height="7"/><use href="#star" x="33" width="7" height="7"/><use href="#star" x="44" width="7" height="7"/></svg></span>
  </div>
</article>

<article class="rank-row row-2">
  <div class="avatar" role="img" aria-label="Portrait photo of the ranked employee"></div>
  <span class="rank-badge">#1 Best</span>
  <span class="person-name">Sam Keller</span>
  <div class="divider"></div>
  <div class="stats">Points: <b>15</b><br>Number of reviews: <b>1</b><br>Smarts<br>Easy to work with<br>Hard worker</div>
  <div class="ratings">
    <span class="view-link">View Details</span>
    <span class="stars"><svg width="52" height="7"><use href="#star" width="7" height="7"/><use href="#star" x="11" width="7" height="7"/><use href="#star" x="22" width="7" height="7"/><use href="#star" x="33" width="7" height="7"/><use href="#star" x="44" width="7" height="7"/></svg></span>
    <span class="stars"><svg width="52" height="7"><use href="#star" width="7" height="7"/><use href="#star" x="11" width="7" height="7"/><use href="#star" x="22" width="7" height="7"/><use href="#star" x="33" width="7" height="7"/><use href="#star" x="44" width="7" height="7"/></svg></span>
    <span class="stars"><svg width="52" height="7"><use href="#star" width="7" height="7"/><use href="#star" x="11" width="7" height="7"/><use href="#star" x="22" width="7" height="7"/><use href="#star" x="33" width="7" height="7"/><use href="#star" x="44" width="7" height="7"/></svg></span>
  </div>
</article>

<article class="rank-row row-3">
  <div class="avatar" role="img" aria-label="Portrait photo of the ranked employee"></div>
  <span class="rank-badge">#1 Best</span>
  <span class="person-name">Sam Keller</span>
  <div class="divider"></div>
  <div class="stats">Points: <b>15</b><br>Number of reviews: <b>1</b><br>Smarts<br>Easy to work with<br>Hard worker</div>
  <div class="ratings">
    <span class="view-link">View Details</span>
    <span class="stars"><svg width="52" height="7"><use href="#star" width="7" height="7"/><use href="#star" x="11" width="7" height="7"/><use href="#star" x="22" width="7" height="7"/><use href="#star" x="33" width="7" height="7"/><use href="#star" x="44" width="7" height="7"/></svg></span>
    <span class="stars"><svg width="52" height="7"><use href="#star" width="7" height="7"/><use href="#star" x="11" width="7" height="7"/><use href="#star" x="22" width="7" height="7"/><use href="#star" x="33" width="7" height="7"/><use href="#star" x="44" width="7" height="7"/></svg></span>
    <span class="stars"><svg width="52" height="7"><use href="#star" width="7" height="7"/><use href="#star" x="11" width="7" height="7"/><use href="#star" x="22" width="7" height="7"/><use href="#star" x="33" width="7" height="7"/><use href="#star" x="44" width="7" height="7"/></svg></span>
  </div>
</article>

<section>
  <h2 class="cta-title">WANT TO SEE MORE RANKINGS?</h2>
  <p class="cta-text"><b>Login</b> or <b>register</b> above.</p>
  <div class="cta-rule login"></div>
  <div class="cta-rule register"></div>
</section>

<footer class="footer">
  <div class="footer-brand">PEER STANDING</div>
  <nav class="footer-nav"><span>SEE TOP RANKINGS</span><span>HOW IT WORKS</span><span>HOW MUCH IS IT</span><span>CONTACT US</span></nav>
  <div class="social"><i></i><i></i><i></i></div>
  <div class="copyright">COPYRIGHT © 2016</div>
</footer>
</body>
</html>
```